Design Mailchimp Ads for Harlow Quill

I am looking to have several Mailchimp ads designed for campaigns we are running starting next week. Mailchimp requires that you use their templates, so if you have experience working with Mailchimp, please let me know. We have an abudance of pictures, logos, etc. that can be downloaded from our FTP site. Thank you.

Target Market(s)

Roofing wholesale market

Colors
fbee3d
add136
9bcb3b
fbed22

Requirements
Must have
• Corporate image, yet creative and crisp, impact. I will need to work one on one briefly with the winning designer to modify these campaigns. Once we have the template completed we will do either 4 or 5 slightly edited versions to reflect the client we are sending it to. The ad will need to have a place holder for our client's logo. We need to advertise free shipping with in the continental U.S. on all full pallet orders. July 1, 2015 - September 30, 2015. It needs to state standard version at the bottom saying this is copyrighted material, etc. It also needs to state Better Parts, Better Performance, Better Products.
Nice to have
• I would like to use green yellow and white as the staple colors, but don't let me block your creativity if you have something else in mind.

```html
<!DOCTYPE html>
<html lang="en">
<head>
<meta charset="utf-8">
<title>Harlow Quill Newsletter</title>
<link href="https://fonts.googleapis.com/css2?family=Arimo:wght@400;700&display=swap" rel="stylesheet">
<style>
:root{
  --lime:#add136;
  --green:#9bcb3b;
  --green-dark:#7fae22;
  --yellow:#fbed22;
  --ink:#1c1c1c;
  --grey:#8a8a8a;
  --text:#777;
  --page:#ececec;
  --white:#ffffff;
  --line:#d9d9d9;
}
*{margin:0;padding:0;box-sizing:border-box}
html,body{width:1200px;height:2184px;overflow:hidden}
body{background:var(--page);font-family:"Arimo",Arial,sans-serif;color:var(--ink);position:relative}
.abs{position:absolute}
.preheader{top:6px;right:48px;font-size:13px;color:var(--grey)}
.preheader a{color:var(--green-dark);text-decoration:none;font-weight:700}

.masthead{top:28px;left:20px;width:1160px;height:252px;
  background:linear-gradient(180deg,#d3e86a 0%,var(--lime) 45%,var(--green) 100%);
  border-bottom:4px solid var(--green-dark)}
.brand{position:absolute;left:52px;top:50px;font-size:78px;font-weight:700;color:#2a2a14;letter-spacing:1px}
.tagline{position:absolute;left:60px;top:150px;font-size:30px;font-weight:700;color:var(--white)}
.slogan{position:absolute;left:60px;top:196px;font-size:20px;font-weight:700;color:#2a2a14}
.client-logo{position:absolute;left:772px;top:52px;width:150px;height:140px;border:2px dashed var(--white);
  display:flex;align-items:center;justify-content:center;text-align:center;font-size:17px;font-weight:700;color:var(--white)}
.issue-date{position:absolute;right:56px;top:40px;text-align:center;color:var(--white)}
.issue-date .day{font-size:118px;font-weight:700;line-height:1}
.issue-date .month{font-size:24px;font-weight:700;margin-top:6px}

.hero{top:284px;left:20px;width:1160px;height:476px;background:var(--white)}
.hero h1{position:absolute;left:52px;top:60px;width:440px;font-size:52px;line-height:1.12;font-weight:400}
.hero p{position:absolute;left:52px;top:196px;width:430px;font-size:20px;line-height:1.45;color:#333}
.btn{position:absolute;left:52px;top:396px;width:164px;height:52px;background:var(--green);color:var(--white);
  font-size:18px;display:flex;align-items:center;justify-content:center;gap:12px}
.hero-media{position:absolute;left:590px;top:32px;width:520px;height:412px;
  background:radial-gradient(ellipse at 50% 45%,#c0542c 0%,#963a1c 55%,#ffffff 78%)}

.section-bar{top:778px;left:20px;width:1160px;height:84px;
  background:linear-gradient(180deg,var(--lime),var(--green));color:var(--white)}
.section-bar h2{position:absolute;left:44px;top:20px;font-size:42px;font-weight:400}
.section-bar a{position:absolute;right:40px;top:30px;font-size:17px;color:var(--white);text-decoration:underline}

.card{left:44px;width:1112px;background:var(--white);border:1px solid var(--line)}
.card h3{position:absolute;font-size:46px;font-weight:700}
.card .date{position:absolute;font-size:17px;color:var(--grey)}
.card p{position:absolute;font-size:19px;line-height:1.5;color:var(--text)}
.card p b{color:#555}
.thumb{position:absolute;width:310px;height:290px;border:1px solid var(--line);background:var(--white);padding:14px}
.thumb span{display:block;width:100%;height:100%;
  background:radial-gradient(ellipse at 50% 50%,#4a4a4a 0%,#1b1b1b 55%,#f2f2f2 80%)}
.ribbon{position:absolute;width:160px;height:36px;font-size:17px;font-weight:700;display:flex;align-items:center;justify-content:center}
.ribbon.left{top:26px;left:-38px;transform:rotate(-45deg)}
.ribbon.right{top:26px;right:-38px;transform:rotate(45deg)}
.ribbon.green{background:var(--green);color:var(--white)}
.ribbon.yellow{background:var(--yellow);color:var(--ink)}
.thumb-wrap{position:absolute;overflow:hidden;width:310px;height:290px}
.price{position:absolute;width:164px;height:160px;background:#f4f4f4;border:1px solid var(--line);text-align:center}
.price .label{font-size:26px;color:var(--grey);padding-top:8px}
.price .amount{margin:6px auto 0;width:130px;height:66px;background:var(--white);border:2px solid var(--green);
  color:var(--green);font-size:48px;font-weight:700;line-height:62px}
.price .cta{position:absolute;left:0;bottom:0;width:100%;height:30px;background:var(--green);color:var(--white);
  font-size:16px;font-weight:700;line-height:30px}

.shipping{top:2036px;left:44px;width:1112px;height:42px;background:var(--yellow);color:var(--ink);
  font-size:18px;display:flex;align-items:center;justify-content:center;gap:8px}
.shipping b{font-weight:700}
.social{top:2094px;left:0;width:1200px;text-align:center;font-size:16px;letter-spacing:2px;color:var(--grey)}
.social b{color:#2a8ad8}
.social .sep{margin:0 22px}
.rule{top:2124px;left:44px;width:1112px;height:1px;background:var(--line)}
.footer-left{top:2140px;left:48px;font-size:15px;color:var(--grey)}
.footer-left a{color:var(--green-dark);text-decoration:none}
.footer-right{top:2140px;right:48px;font-size:15px;color:var(--grey)}
</style>
</head>
<body>

<div class="abs preheader">Having trouble reading this newsletter? <a href="#">Click here</a> to see it in your browser</div>

<header class="abs masthead">
  <div class="brand">Harlow Quill</div>
  <div class="tagline">America's Leader in Solar Powered Ventilation</div>
  <div class="slogan">Better Parts, Better Performance, Better Products</div>
  <div class="client-logo">Client Logo</div>
  <div class="issue-date"><div class="day">15</div><div class="month">Jul, 2015</div></div>
</header>

<section class="abs hero">
  <h1>The Best Product of The Year</h1>
  <p>Curabitur ultricies tristique viverra. Aenean aliquam leo eu nunc pellentesque rutrum. Etiam ac eleifend massa. Fusce hendrerit suscipit mollis. Nam ac libero vehicula massa facilisis varius. Null ampretium fermentum</p>
  <div class="btn">find out more
    <svg width="12" height="12" viewBox="0 0 12 12"><path d="M3 1l6 5-6 5z" fill="#fff"/></svg>
  </div>
  <div class="hero-media" role="img" aria-label="Copper-finished solar powered attic fan with solar panel on top"></div>
</section>

<div class="abs section-bar">
  <h2>Latest Products</h2>
  <a href="#">visit our site</a>
</div>

<article class="abs card" style="top:888px;height:352px">
  <div class="thumb" style="left:16px;top:30px"><span role="img" aria-label="Black solar powered roof vent"></span></div>
  <h3 style="left:374px;top:28px">Your Product Name is Here</h3>
  <div class="date" style="left:376px;top:88px">Wendsday, 07/15/2015</div>
  <p style="left:376px;top:128px;width:520px">Curabitur ultricies tristique viverra. Aenean aliquam leo eu nunc pellentesque rutrum. Etiam ac <b>eleifend</b> massa. Fusce hendrerit suscipit mollis. Nam aclib ero vehicula massa facilisis varius. Null ampretium fermentum egestas. <b>Vestibulum</b> tempus mauris eu nisl venenatis nec faucibus justo iaculis. Cras</p>
  <div class="price" style="left:920px;top:148px"><div class="label">price</div><div class="amount">$25</div><div class="cta">click here</div></div>
</article>

<article class="abs card" style="top:1274px;height:356px">
  <h3 style="left:16px;top:24px">Your Product Name is Here</h3>
  <div class="date" style="left:18px;top:84px">Wendsday, 07/15/2015</div>
  <div class="price" style="left:16px;top:132px"><div class="label">price</div><div class="amount">$25</div><div class="cta">click here</div></div>
  <p style="left:200px;top:120px;width:520px">Curabitur ultricies <b>tristique</b> viverra. Aenean aliquam leo eu nunc pellentesque rutrum. Etiam ac <b>eleifend</b> massa. Fusce hendrerit suscipit mollis. Nam aclib ero vehicula massa facilisis varius. Null ampretium fermentum egestas. <b>Vestibulum</b> tempus mauris eu nisl venenatis nec faucibus justo iaculis. Cras</p>
  <div class="thumb-wrap" style="left:780px;top:36px">
    <div class="thumb" style="left:0;top:0"><span role="img" aria-label="Black solar powered roof vent"></span></div>
    <div class="ribbon right green">10% OFF</div>
  </div>
</article>

<article class="abs card" style="top:1662px;height:358px">
  <div class="thumb-wrap" style="left:16px;top:34px">
    <div class="thumb" style="left:0;top:0"><span role="img" aria-label="Black solar powered roof vent"></span></div>
    <div class="ribbon left yellow">10% OFF</div>
  </div>
  <h3 style="left:374px;top:26px">Your Product Name is Here</h3>
  <div class="date" style="left:376px;top:86px">Wendsday, 07/15/2015</div>
  <p style="left:376px;top:126px;width:520px">Curabitur ultricies tristique viverra. Aenean aliquam leo eu nunc pellentesque rutrum. Etiam ac <b>eleifend</b> massa. Fusce hendrerit suscipit mollis. Nam aclib ero vehicula massa facilisis varius. Null ampretium fermentum egestas. <b>Vestibulum</b> tempus mauris eu nisl venenatis nec faucibus justo iaculis. Cras</p>
  <div class="price" style="left:920px;top:120px"><div class="label">price</div><div class="amount">$25</div><div class="cta">click here</div></div>
</article>

<div class="abs shipping"><b>FREE SHIPPING</b> in the continental U.S. on all full pallet orders &middot; July 1, 2015 – September 30, 2015</div>

<div class="abs social">
  <span>•</span> JOIN US ON <b>PAGEBOARD</b><span class="sep">•</span>FOLLOW US ON <b>CHIRPLINE</b> <span>•</span>
</div>
<div class="abs rule"></div>
<div class="abs footer-left"><a href="#">Click here</a> to unsubscribe this newsletter</div>
<div class="abs footer-right">Copyright © 2015 Harlow Quill. All rights reserved. Copyrighted material.</div>

</body>
</html>
```